Website design and Setup for Real Estate Firm and Going Live

We are a commercial real estate investment firm and are looking for a 6 page website which is informational only. Some text and graphics on each page. We would want the designer to code and launch the website. This website needs to be corporate looking as well as innovative. We are setting up the website on hostivo.

The first page will be a home page with generic commercial real estate look with a link to the following 5 pages on page 1. So page one (the Home Page should have a commercial real estate look with the text linking to the following pages. Page 2 "About Us" with 3 paragraphs describing our firm. Page 3 "Our Platform" with another few paragraphs on due diligence, acquisitions, financing, and management.

Page 4 is "Our Team" highlighting several manager profiles. Page 5 is our "investment Portfolio portal" which will be password protected so not a lot of text, only general graphics and anyone viewing the site casually won't get into the backend, Page 6 is the contact us page. All of the content will be uploaded shortly.

The project includes setting up hyperlinks in the website as well rotating images etc and a final complete live online product. We do not expect to pay for any stock images.

Target Market(s)

Investors, Real Estate Professionals, Brokerages

Industry/Entity Type

Real Estate

Coding

Coded - Design and coding required

Number of Pages Required

5+ page

Requirements
Must have
• Corporate cutting edge design, suitable for a financial corporation.

```html
<!DOCTYPE html>
<html lang="en">
<head>
<meta charset="utf-8">
<title>Meridian</title>
<link href="https://fonts.googleapis.com/css2?family=Poppins:wght@300;400;500;600;700&display=swap" rel="stylesheet">
<style>
:root{
  --gold:#b98e56;
  --gold-dark:#9c7542;
  --navy:#171b35;
  --navy-2:#1f2547;
  --ink:#1e1e1e;
  --muted:#6f6f6f;
  --light:#f5f5f5;
  --white:#ffffff;
  --line:#dcdcdc;
}
*{box-sizing:border-box;margin:0;padding:0}
html,body{width:1200px;height:4520px;overflow:hidden}
body{font-family:'Poppins',sans-serif;color:var(--ink);background:var(--white);position:relative}
section,header,footer{position:absolute;left:0;width:1200px}
.btn{position:absolute;display:inline-flex;align-items:center;justify-content:center;background:var(--gold);color:var(--white);font-size:13px;font-weight:500;letter-spacing:1px;text-transform:uppercase;height:42px;padding:0 28px;white-space:nowrap}
.eyebrow{font-size:14px;letter-spacing:3px;color:var(--gold);text-transform:uppercase;font-weight:500}
.heading{font-size:40px;font-weight:600;color:var(--ink);line-height:1.1}
.rule{width:60px;height:3px;background:var(--gold)}
.body-text{font-size:14px;line-height:1.75;color:var(--muted)}

/* hero */
.hero{top:0;height:752px;background:linear-gradient(180deg,#2a3556 0%,#4a5a7c 40%,#7f8aa1 70%,#3b3f4d 100%)}
.hero-photo{position:absolute;inset:0;background:linear-gradient(160deg,rgba(20,28,55,.55),rgba(40,52,85,.2) 55%,rgba(20,22,30,.6))}
.brand{position:absolute;display:flex;align-items:center;gap:12px;color:var(--white)}
.hero .brand{left:100px;top:30px}
.brand-mark{width:22px;height:22px;background:var(--gold)}
.brand-name{font-size:22px;font-weight:500;letter-spacing:3px;line-height:1;color:var(--white)}
.menu{position:absolute;right:100px;top:38px;display:flex;align-items:center;gap:12px;color:var(--white);font-size:13px;letter-spacing:1px}
.menu-bars{width:30px}
.menu-bars span{display:block;height:2px;background:var(--white);margin:6px 0}
.hero-title{position:absolute;left:100px;top:200px;color:var(--white);font-size:64px;font-weight:700;line-height:1;letter-spacing:1px}
.hero-title span{display:block;font-weight:300;margin-top:6px}
.hero-text{position:absolute;left:100px;top:350px;width:560px;color:var(--white);font-size:17px;line-height:1.5}
.hero .btn{left:100px;top:430px}
.hero-social{position:absolute;left:42px;top:306px;display:flex;flex-direction:column;gap:16px}
.hero-social i{display:block;width:10px;height:10px;border-radius:50%;background:var(--white)}
.hero-tools{position:absolute;right:52px;top:344px;display:flex;flex-direction:column;gap:22px}
.dots{position:absolute;left:0;right:0;top:714px;display:flex;justify-content:center;gap:12px}
.dots i{width:12px;height:12px;border-radius:50%;border:2px solid var(--white)}
.dots i.on{background:var(--white)}

/* firm */
.firm{top:752px;height:616px;background:var(--white)}
.firm-frame{position:absolute;left:240px;top:80px;width:360px;height:440px;border:2px solid var(--gold)}
.firm-photo{position:absolute;left:100px;top:88px;width:468px;height:400px;background:linear-gradient(180deg,#e6e6e6,#c9c9c9)}
.firm-copy{position:absolute;left:648px;top:110px;width:450px}

/* properties */
.properties{top:1368px;height:852px;background:var(--light)}
.center-head{position:absolute;left:0;right:0;text-align:center}
.center-sub{position:absolute;left:300px;width:600px;text-align:center;font-size:14px;line-height:1.7;color:var(--muted)}
.prop-card{position:absolute;display:flex;align-items:flex-end;justify-content:center;padding-bottom:22px;color:var(--white);font-size:17px;font-weight:500;letter-spacing:1px}
.prop-card.apartments{left:100px;top:208px;width:316px;height:412px;background:linear-gradient(180deg,#c8d8ea,#3f4b60 55%,#22272f)}
.prop-card.industries{left:440px;top:232px;width:316px;height:404px;background:linear-gradient(180deg,#bcd6ee,#d49a33 50%,#2b2d33)}
.prop-card.offices{left:780px;top:208px;width:320px;height:412px;background:linear-gradient(180deg,#d5dfe9,#51565f 50%,#1f2226)}

/* approach */
.approach{top:2220px;height:580px;background:var(--white)}
.approach-copy{position:absolute;left:100px;top:80px;width:450px}
.approach-frame{position:absolute;left:600px;top:100px;width:472px;height:380px;border:2px solid var(--gold)}
.approach-photo{position:absolute;left:632px;top:60px;width:468px;height:380px;background:linear-gradient(180deg,#9ec3e6,#cfe0ee 50%,#6b8a66)}

/* roles */
.roles{top:2800px;height:312px;background:linear-gradient(180deg,var(--navy-2),var(--navy))}
.role{position:absolute;top:80px;width:220px;text-align:center;color:var(--white)}
.role svg{display:block;margin:0 auto 12px}
.role h3{font-size:18px;font-weight:500;letter-spacing:2px;margin-bottom:6px}
.role p{font-size:12px;line-height:1.6;color:#c9cbd6}

/* contact */
.contact{top:3112px;height:988px;background:var(--white)}
.city-photo{position:absolute;left:0;top:620px;width:1200px;height:368px;background:linear-gradient(180deg,#ffffff 0%,#d8e4f1 25%,#8fa3bd 65%,#3c4556 100%)}
.contact-info{position:absolute;left:150px;top:308px;width:320px}
.contact-info dt{font-size:14px;font-weight:600;letter-spacing:1px;margin-top:26px}
.contact-info dt:first-child{margin-top:0}
.contact-info dd{font-size:13px;color:var(--muted);line-height:1.6;margin-top:4px}
.follow{display:flex;gap:10px;margin-top:10px}
.follow i{width:34px;height:34px;border-radius:50%;background:#2f6fc0}
.follow i:nth-child(2){background:#2aa4e6}
.follow i:nth-child(3){background:#214c8c}
.follow i:nth-child(4){background:#1f78b4}
.form-card{position:absolute;left:504px;top:288px;width:544px;height:400px;background:var(--white);box-shadow:0 6px 30px rgba(0,0,0,.12);padding:28px 40px}
.form-card h4{font-size:15px;font-weight:600;letter-spacing:1px;margin-bottom:18px}
.field{display:flex;justify-content:space-between;align-items:center;border-bottom:1px solid var(--line);height:56px;font-size:13px;color:var(--muted)}
.field.tall{height:96px;align-items:flex-start;padding-top:20px}
.form-card .btn{right:40px;top:336px}

/* footer */
.site-footer{top:4100px;height:420px;background:var(--navy);color:var(--white)}
.site-footer .brand{left:100px;top:92px}
.footer-social{position:absolute;left:100px;top:200px;display:flex;gap:10px}
.footer-social i{width:34px;height:34px;border-radius:50%;border:1.5px solid var(--white)}
.footer-col{position:absolute;top:74px}
.footer-col h5{font-size:15px;font-weight:500;margin-bottom:8px}
.footer-col .rule{width:36px;height:2px;margin-bottom:16px}
.footer-col li{list-style:none;font-size:12px;color:#c9cbd6;line-height:1.9}
.footer-col .ci{display:flex;gap:10px;align-items:flex-start;margin-bottom:12px;font-size:12px;color:#c9cbd6;line-height:1.5}
.footer-bottom{position:absolute;left:100px;right:100px;top:370px;border-top:1px solid rgba(255,255,255,.15);padding-top:18px;display:flex;justify-content:space-between;font-size:12px;color:#c9cbd6}
</style>
</head>
<body>

<header class="hero">
  <div class="hero-photo" role="img" aria-label="Photograph of a modern glass office tower at dusk"></div>
  <div class="brand"><span class="brand-mark"></span><span class="brand-name">MERIDIAN</span></div>
  <div class="menu">MENU<div class="menu-bars"><span></span><span></span></div></div>
  <div class="hero-social"><i></i><i></i><i></i><i></i></div>
  <div class="hero-tools">
    <svg width="22" height="18" viewBox="0 0 22 18" fill="none" stroke="#fff" stroke-width="2"><path d="M2 9h18M13 2l7 7-7 7"/></svg>
    <svg width="22" height="16" viewBox="0 0 22 16" fill="none" stroke="#fff" stroke-width="2"><rect x="1" y="1" width="20" height="14"/><path d="M1 1l10 8 10-8"/></svg>
    <svg width="20" height="20" viewBox="0 0 20 20" fill="none" stroke="#fff" stroke-width="2"><path d="M4 1h4l2 5-3 2a11 11 0 005 5l2-3 5 2v4a2 2 0 01-2 2A17 17 0 012 3a2 2 0 012-2z"/></svg>
  </div>
  <h1 class="hero-title">COMMERCIAL<span>REAL ESTATE</span></h1>
  <p class="hero-text">Lorem ipsum dolor sit amet, consectetur adipiscing elit, sed do eiusmod tempor incididunt ut</p>
  <a class="btn">Explore Our Projects</a>
  <div class="dots"><i class="on"></i><i></i><i></i></div>
</header>

<section class="firm">
  <div class="firm-frame"></div>
  <div class="firm-photo" role="img" aria-label="Portrait of a businessman in a dark suit"></div>
  <div class="firm-copy">
    <div class="eyebrow">About Us</div>
    <h2 class="heading" style="margin-top:6px">OUR FIRM</h2>
    <div class="rule" style="margin:14px 0 22px"></div>
    <p class="body-text">Lorem ipsum dolor sit amet, consectetur adipiscing elit, sed do eiusmod tempor incididunt ut labore et dolore magna aliqua. Quis ipsum suspendisse ultrices gravida. Risus commodo viverra maecenas accumsan lacus vel facilisis.</p>
    <p class="body-text" style="margin-top:16px">Lorem ipsum dolor sit amet, consectetur adipiscing elit, sed do eiusmod tempor incididunt ut labore et dolore magna aliqua. Quis ipsum suspendisse ultrices gravida. Risus commodo viverra maecenas accumsan lacus vel facilisis.</p>
  </div>
  <a class="btn" style="left:648px;top:450px">Learn More</a>
</section>

<section class="properties">
  <h2 class="heading center-head" style="top:78px">OUR PROPERTIES</h2>
  <p class="center-sub" style="top:134px">At vero eos et accusamus et iustoghistimo ducimus qui blanditiis praesentium voluptatum deleniti atque corrupti quos dolores</p>
  <div class="prop-card apartments" role="img" aria-label="Photograph of a dark modern apartment building">APARTMENTS</div>
  <div class="prop-card industries" role="img" aria-label="Photograph of a modern building with yellow facade panels">INDUSTRIES</div>
  <div class="prop-card offices" role="img" aria-label="Photograph of a modern office building">OFFICES</div>
  <a class="btn" style="left:524px;top:684px;width:152px">See All</a>
</section>

<section class="approach">
  <div class="approach-copy">
    <div class="eyebrow">Commercial Real Estate</div>
    <h2 class="heading" style="margin-top:6px">OUR APPROACH</h2>
    <div class="rule" style="margin:14px 0 22px"></div>
    <p class="body-text">Lorem ipsum dolor sit amet, consectetur adipiscing elit, sed do eiusmod tempor incididunt ut labore et dolore magna aliqua. Quis ipsum suspendisse ultrices gravida. Risus commodo viverra maecenas accumsan lacus vel facilisis.</p>
    <p class="body-text" style="margin-top:16px">Lorem ipsum dolor sit amet, consectetur adipiscing elit, sed do eiusmod tempor incididunt ut labore et dolore magna aliqua. Quis ipsum suspendisse ultrices gravida. Risus commodo viverra maecenas accumsan lacus vel facilisis.</p>
  </div>
  <a class="btn" style="left:100px;top:416px">Learn More</a>
  <div class="approach-frame"></div>
  <div class="approach-photo" role="img" aria-label="Photograph of a glass office tower with palm trees"></div>
</section>

<section class="roles">
  <div class="role" style="left:104px">
    <svg width="44" height="56" viewBox="0 0 44 56" fill="none" stroke="#c9cbd6" stroke-width="1.5"><path d="M6 55V10L22 2l16 8v45M2 55h40M14 18h4M26 18h4M14 28h4M26 28h4M14 38h4M26 38h4M18 55v-8h8v8"/></svg>
    <h3>OWNER</h3><p>Lorem ipsum dolor sit amet, consectetur adipiscing sed do eiusmod tempor incididunt ut labore</p>
  </div>
  <div class="role" style="left:344px">
    <svg width="44" height="56" viewBox="0 0 44 56" fill="none" stroke="#c9cbd6" stroke-width="1.5"><path d="M10 55V6h24v49M4 55h36M16 14h4M24 14h4M16 24h4M24 24h4M16 34h4M24 34h4M16 44h4M24 44h4"/></svg>
    <h3>DEVELOPER</h3><p>Lorem ipsum dolor sit amet, consectetur adipiscing sed do eiusmod tempor incididunt ut labore</p>
  </div>
  <div class="role" style="left:600px">
    <svg width="56" height="56" viewBox="0 0 56 56" fill="none" stroke="#c9cbd6" stroke-width="1.5"><rect x="4" y="16" width="48" height="26"/><circle cx="28" cy="29" r="7"/><path d="M10 22v14M46 22v14"/></svg>
    <h3>INVESTOR</h3><p>Lorem ipsum dolor sit amet, consectetur adipiscing sed do eiusmod tempor incididunt ut labore</p>
  </div>
  <div class="role" style="left:856px">
    <svg width="56" height="56" viewBox="0 0 56 56" fill="none" stroke="#c9cbd6" stroke-width="1.5"><circle cx="22" cy="32" r="12"/><circle cx="22" cy="32" r="4"/><circle cx="40" cy="16" r="8"/><circle cx="40" cy="16" r="3"/></svg>
    <h3>OPERATOR</h3><p>Lorem ipsum dolor sit amet, consectetur adipiscing sed do eiusmod tempor incididunt ut labore</p>
  </div>
</section>

<section class="contact">
  <div class="city-photo" role="img" aria-label="Photograph of a city skyline with a bridge over a river"></div>
  <h2 class="heading center-head" style="top:68px">GET IN TOUCH</h2>
  <p class="center-sub" style="top:122px">At vero eos et accusamus et iustoghistimo ducimus qui blanditiis praesentium voluptatum deleniti atque corrupti quos dolores</p>
  <dl class="contact-info">
    <dt>LOCATION:</dt><dd>123 Your Adress Goes Here,<br>CA, 1234567</dd>
    <dt>EMAIL ADDRESS:</dt><dd>info@meridiancre.com</dd>
    <dt>CALL US NOW:</dt><dd>+123 456 7890</dd>
    <dt>FOLLOW NOW:</dt><dd><div class="follow"><i></i><i></i><i></i><i></i></div></dd>
  </dl>
  <div class="form-card">
    <h4>DROP YOUR MESSAGE</h4>
    <div class="field">Jonathan Doe<svg width="16" height="16" viewBox="0 0 16 16" fill="none" stroke="#888" stroke-width="1.3"><circle cx="8" cy="5" r="3.5"/><path d="M1 15c1-4 13-4 14 0"/></svg></div>
    <div class="field">Email Address<svg width="18" height="13" viewBox="0 0 18 13" fill="none" stroke="#888" stroke-width="1.3"><rect x="1" y="1" width="16" height="11"/><path d="M1 1l8 6 8-6"/></svg></div>
    <div class="field tall">Message<svg width="18" height="16" viewBox="0 0 18 16" fill="none" stroke="#888" stroke-width="1.3"><path d="M1 2h16v9H7l-4 4v-4H1z"/></svg></div>
    <a class="btn">Contact Us Now</a>
  </div>
</section>

<footer class="site-footer">
  <div class="brand"><span class="brand-mark"></span><span class="brand-name">MERIDIAN</span></div>
  <div class="footer-social"><i></i><i></i><i></i><i></i></div>
  <div class="footer-col" style="left:432px"><h5>Quick Link</h5><div class="rule"></div>
    <ul><li>Home</li><li>About Us</li><li>Our Platform</li><li>Our Team</li><li>Investment Portfolio</li><li>Contact us</li></ul></div>
  <div class="footer-col" style="left:668px"><h5>Other Link</h5><div class="rule"></div>
    <ul><li>Who We Are</li><li>Career</li><li>News</li><li>Resources</li><li>Contact</li></ul></div>
  <div class="footer-col" style="left:852px"><h5>Contact Info</h5><div class="rule"></div>
    <div class="ci"><svg width="12" height="16" viewBox="0 0 12 16" fill="#b98e56"><path d="M6 0a6 6 0 016 6c0 4-6 10-6 10S0 10 0 6a6 6 0 016-6z"/></svg><span>123 Your Adress Goes Here<br>CA, 1234567</span></div>
    <div class="ci"><svg width="13" height="13" viewBox="0 0 20 20" fill="#b98e56"><path d="M4 1h4l2 5-3 2a11 11 0 005 5l2-3 5 2v4a2 2 0 01-2 2A17 17 0 012 3a2 2 0 012-2z"/></svg><span>+123 456 7890</span></div>
    <div class="ci"><svg width="14" height="11" viewBox="0 0 18 13" fill="#b98e56"><rect x="0" y="0" width="18" height="13"/></svg><span>info@meridiancre.com</span></div>
  </div>
  <div class="footer-bottom"><span>Copyright © 2021 - meridian. All Right Reserved</span><span>Privacy Policy &nbsp;|&nbsp; Terms &amp; Conditions</span></div>
</footer>

</body>
</html>
```